依頼詳細
発泡スチロール製品の事例を紹介するリーフレットのデザインをお願い致します。
発泡スチロールの箱をいろいろな業種の方にご利用いただいております。いろいろな発泡スチロールの利用状況とお客様の声を今後DMとして発送を計画しております。
シリーズとして使えるようにしていきたいと考えております。今回は緑系統で、今後は色を替えることも想定してデザインをお願いできればと思います。
記載項目
社名、電話番号、ホームページアドレス、所在地
サイズ
A4
ページ数
片面
希望イメージ
シンプル 複雑
単色 カラフル
暗い 明るい
日常 高級
遊び心 厳粛
未来的 伝統的
女性的 男性的
希望する色
緑系、ロゴの色
納品ファイル
• イラストレーター形式 (.ai)
補足説明
ロゴデータはありません。添付書類参照下さい。
お世話になっております。コンペ参加者の皆様大変申し訳ありませんが、もう少し提案数が必要なため提案期日を10日延長いたしました。
現在参加されている方には大変申し訳ありませんがご理解いただきますようお願い申し上げます。
■ 選んだ理由

大変素晴らしいデザインありがとうございました。
お客様も大変悩まれておりましたが、大変気に入って頂けました。

■ 提案者全員のお礼・コメント

沢山のご提案ありがとうございました。
今後共デザインコンペを行ってまいりますのでよろしくお願いいたします。

```html
<!DOCTYPE html>
<html lang="ja">
<head>
<meta charset="utf-8">
<title>FORMIA通信 Vol.1</title>
<link rel="stylesheet" href="https://fonts.googleapis.com/css2?family=Noto+Sans+JP:wght@400;500;700;900&family=Noto+Serif+JP:wght@700;900&display=swap">
<style>
  :root{
    --green:#2f8a3c;
    --green-dark:#1f6a2c;
    --red:#d8262d;
    --brown:#8a5a2b;
    --ink:#222;
    --grey:#f1f1ef;
    --line:#cfcfcf;
    --white:#fff;
  }
  *{box-sizing:border-box;margin:0;padding:0}
  html,body{width:848px;height:1200px;overflow:hidden;background:var(--white)}
  body{font-family:"Noto Sans JP",sans-serif;color:var(--ink);position:relative}
  .sheet{position:absolute;inset:0;width:848px;height:1200px}

  .masthead{position:absolute;left:0;top:0;width:848px;height:90px;background:var(--grey)}
  .masthead-title{position:absolute;left:40px;top:18px;font-weight:900;font-size:38px;color:var(--green-dark);letter-spacing:1px}
  .masthead-title .vol{font-size:16px;margin-left:6px;color:var(--green)}
  .masthead-tagline{position:absolute;right:36px;top:24px;border:1.5px solid var(--green-dark);border-radius:20px;padding:5px 16px;font-size:13px;font-weight:700;color:var(--green-dark);background:var(--white)}
  .case-label{position:absolute;right:40px;top:66px;font-size:11px;color:#555}

  .request{position:absolute;left:0;top:90px;width:848px;height:290px;background:var(--grey)}
  .request-box{position:absolute;left:40px;top:20px;width:768px;height:248px;border:3px solid var(--red);background:var(--white)}
  .request-tab{position:absolute;left:18px;top:-14px;background:var(--red);color:var(--white);font-size:14px;font-weight:700;padding:3px 16px;border-radius:3px}
  .request-headline{position:absolute;left:0;right:0;top:34px;text-align:center;font-family:"Noto Serif JP",serif;font-weight:900;font-size:50px;line-height:1.3;color:var(--ink);letter-spacing:1px}
  .request-headline .accent{border-bottom:3px solid var(--red)}
  .request-body{position:absolute;left:36px;right:36px;top:180px;font-size:11.5px;line-height:1.75;color:#444}

  .proposal-pill{position:absolute;left:274px;top:402px;width:300px;height:36px;background:var(--green);color:var(--white);border-radius:18px;text-align:center;font-size:16px;font-weight:700;line-height:36px}
  .proposal-lead{position:absolute;left:40px;right:40px;top:450px;text-align:center;font-size:13px;color:#333}
  .point{position:absolute;top:482px;width:368px;height:54px;background:var(--green);color:var(--white);text-align:center;font-size:24px;font-weight:900;line-height:54px;border-radius:4px}
  .point-1{left:40px}.point-2{left:440px}
  .point-note{position:absolute;top:548px;width:368px;text-align:center;font-size:15px;font-weight:700;line-height:1.6}
  .point-note-1{left:40px}.point-note-2{left:440px}
  .point-note .brown{color:var(--brown)}

  .product-photo{position:absolute;left:40px;top:620px;width:368px;height:260px;background:linear-gradient(160deg,#efe6d6,#c9a77a 55%,#8a5a2b);border-radius:3px}
  .adopted{position:absolute;left:28px;top:606px;width:64px;height:30px;background:var(--red);color:var(--white);font-weight:900;font-size:16px;text-align:center;line-height:30px;border-radius:3px}

  .voice{position:absolute;left:440px;top:620px;width:368px;height:260px;border:1.5px solid var(--line);background:var(--white)}
  .voice-title{position:absolute;left:18px;top:14px;font-size:17px;font-weight:900;color:var(--red)}
  .voice-body{position:absolute;left:18px;right:18px;top:46px;font-size:11.5px;line-height:1.8;color:#333}
  .voice-body .hl{color:var(--red);font-weight:700}
  .voice-photo{position:absolute;right:14px;bottom:12px;width:86px;height:70px;background:linear-gradient(180deg,#d8d8d2,#9a9a92)}

  .cta{position:absolute;left:0;top:904px;width:848px;height:96px;background:var(--green)}
  .cta-main{position:absolute;left:0;right:0;top:14px;text-align:center;color:var(--white);font-size:26px;font-weight:900;letter-spacing:1px}
  .cta-sub{position:absolute;left:0;right:0;top:58px;text-align:center;color:var(--white);font-size:13px}

  .contact-label{position:absolute;left:40px;top:1058px;font-size:13px;font-weight:700;line-height:1.5;color:var(--green-dark)}
  .phone{position:absolute;left:148px;top:1042px;display:flex;align-items:center;gap:8px;font-size:40px;font-weight:900;color:var(--ink);letter-spacing:1px;line-height:1.2}
  .phone-hours{position:absolute;left:194px;top:1100px;font-size:10px;color:#555}

  .divider{position:absolute;left:540px;top:1036px;width:1px;height:110px;background:var(--line)}
  .brand{position:absolute;left:560px;top:1034px;display:flex;align-items:center;gap:8px;line-height:1.2}
  .brand-dot{width:14px;height:14px;background:var(--green);border-radius:50%;flex:none}
  .brand-name{font-size:22px;font-weight:700;color:var(--green-dark)}
  .brand-tag{position:absolute;left:560px;top:1070px;font-size:10px;color:#555}
  .address{position:absolute;left:560px;top:1090px;font-size:10px;line-height:1.6;color:#444}
  .web{position:absolute;left:560px;top:1126px;font-size:11px;color:var(--green-dark)}

  .footer-bar{position:absolute;left:0;bottom:0;width:848px;height:14px;background:var(--green-dark)}
</style>
</head>
<body>
<div class="sheet">

  <header class="masthead">
    <div class="masthead-title">FORMIA通信<span class="vol">Vol.1</span></div>
    <div class="masthead-tagline">「40年以上の経験」と「豊富な製品」で、アイデアいっぱい</div>
    <div class="case-label">アイス専用発泡スチロール事例</div>
  </header>

  <section class="request">
    <div class="request-box">
      <div class="request-tab">お客様からのご要望</div>
      <h1 class="request-headline">高級アイスクリームに合った<br><span class="accent">保冷容器が欲しい。</span></h1>
      <p class="request-body">新商品の発売にあたり、手作りにこだわった高級アイスクリーム「雅アイス」を全国へお届けするため、見た目の上品さと保冷性能を両立できる容器を探していました。少ない数量からでも対応してもらえる会社を求めていました。</p>
    </div>
  </section>

  <section class="proposal">
    <div class="proposal-pill">フォルミアからのご提案</div>
    <p class="proposal-lead">提案チームが様々な検討・考察を重ね、下記のようなパッケージのご提案をし、採用していただきました。</p>
    <div class="point point-1">見た目・高級感</div>
    <div class="point point-2">少ロット・性能</div>
    <p class="point-note point-note-1">外観は、高級感を出せる<br><span class="brown">ブラウンカラー</span>製品を選定</p>
    <p class="point-note point-note-2">性能・コスト面から当社既製品で<br>一番適していると思われる製品を選定</p>
  </section>

  <div class="product-photo" role="img" aria-label="ブラウンの発泡スチロール箱にアイスカップが並んだ採用パッケージの写真"></div>
  <div class="adopted">採用</div>

  <section class="voice">
    <h2 class="voice-title">お客様の声</h2>
    <p class="voice-body">「発泡スチロール=安価」のイメージがありましたが、<span class="hl">ブラウンの色合いで高級感が出て</span>、商品の価値が伝わる箱になりました。少ない数量から対応いただけたので、在庫の心配もなく助かっています。<span class="hl">フォルミアの総合的な提案力</span>に大変満足しています。</p>
    <div class="voice-photo" role="img" aria-label="ご担当者様の写真"></div>
  </section>

  <section class="cta">
    <p class="cta-main">ご要望・お悩みごと、ぜひお聞かせください。</p>
    <p class="cta-sub">フォルミアは全力で解決のお手伝いをさせていただきます。</p>
  </section>

  <footer>
    <p class="contact-label">お気軽に<br>お問合せください</p>
    <div class="phone">
      <svg width="36" height="36" viewBox="0 0 24 24" aria-hidden="true"><path fill="#222" d="M6.6 10.8a15.1 15.1 0 0 0 6.6 6.6l2.2-2.2c.3-.3.7-.4 1-.2 1.1.4 2.3.6 3.6.6.6 0 1 .4 1 1V20c0 .6-.4 1-1 1A17 17 0 0 1 3 4c0-.6.4-1 1-1h3.5c.6 0 1 .4 1 1 0 1.3.2 2.5.6 3.6.1.3 0 .7-.2 1z"/></svg>
      0120-48-7315
    </div>
    <p class="phone-hours">受付時間 / 平日 8:30〜17:30（土日祝休）</p>

    <div class="divider"></div>
    <div class="brand"><span class="brand-dot"></span><span class="brand-name">株式会社フォルミア</span></div>
    <p class="brand-tag">発泡スチロール・保冷容器の企画・製造・販売</p>
    <p class="address">〒321-0000 栃木県緑ケ丘市中央町1-2-3<br>TEL 0120-48-7315 ／ FAX 0120-48-7316</p>
    <p class="web">www.formia-pack.jp</p>
    <div class="footer-bar"></div>
  </footer>

</div>
</body>
</html>
```